Business Card, Stationary with Shark Logo for Personal Injury Lawyer

I need business cards and stationery with a shark logo for my Personal Injury Law Practice. Has to have this written on it:
Martin K. Hollis
Injury Lawyer
The Corvell Building
718 Tandy Street
Providence, Rhode Island 02908
401-627-4193
Martinhollis.com

Contact Information for Business Card

Martin K. Hollis, Injury Lawyer, address, 401-627-4193, martinhollis.com

```html
<!DOCTYPE html>
<html lang="en">
<head>
<meta charset="utf-8">
<title>Martin K. Hollis – Business Card</title>
<link href="https://fonts.googleapis.com/css2?family=Montserrat:wght@400;600;800&display=swap" rel="stylesheet">
<style>
  :root {
    --navy: #2b2663;
    --ink: #222222;
    --paper: #ffffff;
    --backdrop: #a7abad;
    --fin-soft: #5a558c;
  }
  * { margin: 0; padding: 0; box-sizing: border-box; }
  html, body { width: 1200px; height: 928px; overflow: hidden; }
  body {
    background: var(--backdrop);
    font-family: "Montserrat", sans-serif;
    position: relative;
  }
  .card {
    position: absolute;
    left: 266px;
    width: 670px;
    height: 386px;
    background: var(--paper);
    border-radius: 18px;
    overflow: hidden;
  }
  .card--front { top: 58px; height: 383px; }
  .card--back { top: 484px; }

  .wordmark {
    position: absolute;
    color: var(--navy);
    font-weight: 800;
    text-transform: uppercase;
    line-height: 1;
  }
  .card--front .wordmark {
    left: 0; right: 0; top: 118px;
    text-align: center;
  }
  .wordmark__line { display: block; }
  .card--front .wordmark__first { font-size: 34px; letter-spacing: 0.5px; }
  .card--front .wordmark__last { font-size: 64px; letter-spacing: 1px; margin-top: 4px; }
  .card--front .wordmark__role { font-size: 20px; letter-spacing: 9px; margin-top: 10px; }

  .social {
    position: absolute;
    top: 322px; left: 0; right: 0;
    display: flex; justify-content: center; gap: 7px;
  }
  .social__dot {
    width: 32px; height: 32px; border-radius: 50%;
    background: var(--navy);
  }

  .card--back .wordmark { left: 42px; top: 50px; }
  .card--back .wordmark__first { font-size: 27px; }
  .card--back .wordmark__last { font-size: 50px; margin-top: 3px; }
  .card--back .wordmark__role { font-size: 15px; letter-spacing: 6.5px; margin-top: 8px; }

  .contact {
    position: absolute;
    left: 44px; top: 206px;
    font-size: 16px;
    color: var(--ink);
    letter-spacing: 1px;
  }
  .contact__row { margin-bottom: 12px; }
  .contact__label { color: var(--navy); font-weight: 600; }
  .contact__address { margin-top: 19px; line-height: 22px; margin-left: -2px; }
  .contact__building { display: block; color: var(--navy); font-weight: 600; margin-bottom: 2px; }

  .fin-area {
    position: absolute;
    left: 420px; top: 136px;
    width: 198px; height: 228px;
    background: linear-gradient(180deg, var(--fin-soft), var(--navy));
    border-radius: 6px 6px 0 0;
  }
  .sea-band {
    position: absolute;
    left: 0; right: 0; bottom: 0;
    height: 22px;
    background: var(--navy);
  }
</style>
</head>
<body>
  <section class="card card--front">
    <div class="wordmark">
      <span class="wordmark__line wordmark__first">Martin K.</span>
      <span class="wordmark__line wordmark__last">Hollis</span>
      <span class="wordmark__line wordmark__role">Injury Lawyer</span>
    </div>
    <div class="social" aria-label="Social media links">
      <span class="social__dot"></span>
      <span class="social__dot"></span>
      <span class="social__dot"></span>
    </div>
  </section>

  <section class="card card--back">
    <div class="wordmark">
      <span class="wordmark__line wordmark__first">Martin K.</span>
      <span class="wordmark__line wordmark__last">Hollis</span>
      <span class="wordmark__line wordmark__role">Injury Lawyer</span>
    </div>

    <div class="contact">
      <p class="contact__row"><span class="contact__label">Call Or Text:</span> 401-627-4193</p>
      <p class="contact__row"><span class="contact__label">Visit:</span> Martinhollis.com</p>
      <p class="contact__address">
        <span class="contact__building">The Corvell Building</span>
        718 Tandy Street<br>
        Providence, Rhode Island 02908
      </p>
    </div>

    <div class="fin-area" role="img" aria-label="Large shark fin rising from the water"></div>
    <div class="sea-band" role="img" aria-label="Water line along the bottom edge"></div>
  </section>
</body>
</html>
```